Worksite Kitbag - uFone app for tradespeople - UI design

Worksite Kitbag is an uFone app for tradespeople (builders, carpenters, electricians, etc) which provides a range of tools that will assist with typical tasks, such as the calculation of unit conversion and spatial/volumetric/electrical measurements. The application also makes use of instruments available in the smartphone device to provide useful tools such as a spirit level, compass and torch.

The product is a simple menu-based application consisting of a number of menu and function screens. Each menu item will navigate the user to the function screen applicable to that menu item. Each function screen will contain the necessary inputs and features for perform its stated function.

The user interface should be designed with the tradesperson user in mind and as such should be simple, intuitive and durable with respect to its usability, interface design and branding elements.

Target Market(s)

Tradespeople (builders, carpenters, electricians, etc)

Industry/Entity Type

Trade

Font styles to use
Sans Serif

Requirements
Must have
• Refer to attached wireframes document...
• - Simple design
• - Consistent layout and theme
• - Screens and icons
Should not have
• - Tacky 3D images and textured backgrounds

```html
<!DOCTYPE html>
<html lang="en">
<head>
<meta charset="utf-8">
<title>Worksite Kitbag – mobile app UI</title>
<link rel="stylesheet" href="https://fonts.googleapis.com/css2?family=Fira+Sans+Condensed:wght@300;400;500&display=swap">
<style>
  :root {
    --orange: #f29d12;
    --ink: #0c0c0c;
    --panel: #1a1a1a;
    --paper: #f2f2f2;
    --text-dark: #1e1e1e;
    --muted: #444444;
  }
  * { box-sizing: border-box; margin: 0; padding: 0; }
  html, body { width: 1200px; height: 995px; overflow: hidden; }
  body {
    position: relative;
    font-family: "Fira Sans Condensed", "Arial Narrow", sans-serif;
    background: linear-gradient(180deg, #2b2b2b 175px, #161616 600px, #050505 995px);
  }
  .top-band {
    position: absolute; left: 0; top: 0; width: 1200px; height: 175px;
    background: linear-gradient(180deg, #101010, #0a0a0a);
  }
  .wordmark {
    color: var(--orange); font-weight: 400; letter-spacing: -0.3px;
    text-transform: uppercase; white-space: nowrap;
  }
  .top-band .wordmark { position: absolute; left: 55px; top: 71px; font-size: 40px; line-height: 1; }

  .screen { position: absolute; overflow: hidden; background: var(--panel); }
  .screen-menu { left: 106px; top: 352px; width: 300px; height: 532px; }
  .screen-splash { left: 434px; top: 232px; width: 332px; height: 588px; }
  .screen-contact { left: 795px; top: 352px; width: 300px; height: 532px; background: var(--paper); }

  .status-bar {
    position: absolute; left: 0; top: 0; width: 100%; height: 20px;
    display: flex; justify-content: space-between; align-items: center;
    padding: 0 10px; font-size: 9px; color: var(--orange); background: var(--ink);
    z-index: 2;
  }
  .screen-splash .status-bar { background: transparent; }
  .status-bar .battery { display: inline-block; width: 16px; height: 7px; border: 1px solid var(--orange); margin-left: 3px; vertical-align: middle; position: relative; }
  .status-bar .battery::after { content: ""; position: absolute; left: 1px; top: 1px; width: 9px; height: 3px; background: var(--orange); }

  .backdrop {
    position: absolute; inset: 0;
    background: linear-gradient(160deg, #2c2c2c 0%, #1b1b1b 35%, #262626 55%, #141414 100%);
  }

  .app-header {
    position: absolute; left: 0; top: 20px; width: 100%; height: 64px;
    background: var(--ink); display: flex; align-items: center; justify-content: center; z-index: 2;
  }
  .screen-menu .app-header { border-bottom: 2px solid var(--orange); }
  .app-header .wordmark { font-size: 23px; }
  .app-header .mail { position: absolute; right: 24px; top: 24px; }
  .app-header .back { position: absolute; left: 18px; top: 23px; }
  .app-header .title { color: var(--orange); font-size: 21px; font-weight: 300; text-transform: uppercase; }

  .tools-icon { position: absolute; left: 124px; top: 120px; }
  .tools-heading {
    position: absolute; left: 0; top: 175px; width: 100%; text-align: center;
    color: var(--orange); font-size: 13px; font-weight: 300; text-transform: uppercase;
  }
  .tool-list { position: absolute; left: 28px; top: 221px; width: 244px; list-style: none; }
  .tool-list li {
    height: 49px; margin-bottom: 6.5px; border: 1px solid var(--orange);
    display: flex; align-items: center; justify-content: center;
    color: var(--orange); font-size: 16px; font-weight: 300;
  }
  .screen-menu .footer-bar { position: absolute; left: 0; bottom: 0; width: 100%; height: 5px; background: var(--orange); }

  .splash-sheen {
    position: absolute; inset: 0;
    background: linear-gradient(115deg, transparent 42%, rgba(255,255,255,0.05) 42%, rgba(255,255,255,0.02) 70%, transparent 70%);
  }
  .screen-splash .wordmark { position: absolute; left: 0; top: 250px; width: 100%; text-align: center; font-size: 33px; }
  .splash-legal {
    position: absolute; left: 30px; bottom: 22px; width: 272px; text-align: center;
    color: #5c5c5c; font-size: 6px; line-height: 1.35; text-transform: uppercase;
  }

  .contact-body { position: absolute; left: 0; top: 138px; width: 100%; text-align: center; }
  .contact-body .wordmark { font-size: 23px; margin-bottom: 14px; }
  .contact-body p { color: var(--text-dark); font-size: 15px; font-weight: 400; line-height: 20px; padding: 0 20px; }
  .button {
    position: absolute; left: 28px; width: 244px; height: 48px; background: var(--orange);
    color: #fff; font-size: 15px; font-weight: 300; display: flex; align-items: center; justify-content: center;
  }
  .button-website { top: 267px; }
  .button-rate { top: 323px; }
  .contact-credit {
    position: absolute; right: 27px; top: 481px; text-align: left;
    color: var(--muted); font-size: 10px; line-height: 13px;
  }
</style>
</head>
<body>

<header class="top-band">
  <div class="wordmark">Worksite Kitbag</div>
</header>

<section class="screen screen-menu">
  <div class="backdrop" role="img" aria-label="Blurred dark worksite photograph behind the menu"></div>
  <div class="status-bar"><span>●○○○○ 3</span><span>16:05</span><span>67% <i class="battery"></i></span></div>
  <div class="app-header">
    <span class="wordmark">Worksite Kitbag</span>
    <svg class="mail" width="16" height="12" viewBox="0 0 16 12" fill="none" stroke="#f29d12" stroke-width="1.5">
      <rect x="1" y="1" width="14" height="10"/><path d="M1 1l7 6 7-6"/>
    </svg>
  </div>
  <svg class="tools-icon" width="52" height="40" viewBox="0 0 52 40">
    <path d="M18 8V3h16v5" fill="none" stroke="#f29d12" stroke-width="3"/>
    <rect x="1" y="8" width="50" height="31" rx="3" fill="#f29d12"/>
    <rect x="1" y="20" width="50" height="2" fill="#1a1a1a"/>
    <rect x="22" y="17" width="8" height="7" fill="#f29d12" stroke="#1a1a1a" stroke-width="1.5"/>
  </svg>
  <div class="tools-heading">Choose your working tools</div>
  <ul class="tool-list">
    <li>Unit Conversion</li>
    <li>Measurement Calculation</li>
    <li>Spirit Level</li>
    <li>Compass</li>
    <li>Torch</li>
  </ul>
  <div class="footer-bar"></div>
</section>

<section class="screen screen-splash">
  <div class="backdrop" role="img" aria-label="Blurred dark photograph of tools on a workbench"></div>
  <div class="splash-sheen"></div>
  <div class="status-bar"><span>●○○○○ 3</span><span>16:05</span><span>67% <i class="battery"></i></span></div>
  <div class="wordmark">Worksite Kitbag</div>
  <div class="splash-legal">
    (C) 2015, Worksite Kitbag<br>
    Built for builders, carpenters and electricians who need<br>
    dependable tools on every worksite, every day.
  </div>
</section>

<section class="screen screen-contact">
  <div class="status-bar"><span>●○○○○ 3</span><span>16:05</span><span>67% <i class="battery"></i></span></div>
  <div class="app-header">
    <svg class="back" width="22" height="18" viewBox="0 0 22 18" fill="none" stroke="#f29d12" stroke-width="1.8">
      <path d="M21 9H2M9 2L2 9l7 7"/>
    </svg>
    <span class="title">Contact us</span>
  </div>
  <div class="contact-body">
    <div class="wordmark">Worksite Kitbag</div>
    <p>For feedback and suggestions,<br>please visit our website. Dont forget to<br>rate our apps.</p>
  </div>
  <div class="button button-website">Visit website</div>
  <div class="button button-rate">Rate us</div>
  <div class="contact-credit">Brought to you by Quillbrook IT Solutions<br>© 2015. All rights reserved.</div>
</section>

</body>
</html>
```